Business Consultants - Require an A4 size presentation folder with inserts for a new exciting Standa

We have developed a service/product where we help small and medium businesses to draft up their policies & procedures manual for their business. This manual has everything in it on how to run their business. From how to answer the phone, to how to process invoices, through to HR information, and marketing plans.

We need a professional but modern looking presentation folder to house all this information. The size will be A4. Inside we will have up to 12 inserts to seperate the different chapters/topic. For example. Sales, Marketing, Administration, Operations, Finance.

Each folder will be branded with the client logo and name on the front, hence it does need to be relativity simple and neutral as to not clash with their colours etc.

We will have our Logo and contact details on the back of the folder.

The design aspect may well come for the chapter inserts. Again the actual tabs will need to be neutral so that we can write on them so that when you open the front cover you can quickly go the chapter you need.

Be warned I do not want any generic design gallery type designs. They stand out as cheap and nasty. I need you actually put some thought into these !!!

Attached is our Logo, and a two photos of the sort of shape and size of the anticipated folders.

Target Market(s)

Small & Medium Brick & Mortar Business Owners

Industry/Entity Type

Business Consultant

Colors

Designer to choose colors to be used in the design.

Requirements
Must have
• Must be clean, crisp, but with some cool simple design elements
Should not have
• Too many bold colours as it will clash with our client logos, which we have no control over what colour they are

```html
<!DOCTYPE html>
<html lang="en">
<head>
<meta charset="utf-8">
<title>Administration Chapter Cover</title>
<link rel="stylesheet" href="https://fonts.googleapis.com/css2?family=Arimo:wght@400;700&display=swap">
<style>
  :root {
    --page-bg: #ffffff;
    --cover-paper: #fbf9ee;
    --cover-edge: #3a3a3c;
    --accent-blue: #2ba3dd;
    --ink: #2b2b2b;
    --brand-grey: #6d6e70;
    --rule: #5a5a5a;
    --art-dark: #3c3c3e;
    --art-light: #c9c9cb;
  }
  * { margin: 0; padding: 0; box-sizing: border-box; }
  html, body {
    width: 1200px;
    height: 1200px;
    overflow: hidden;
    background: var(--page-bg);
    font-family: "Arimo", Arial, sans-serif;
  }
  .canvas {
    position: relative;
    width: 1200px;
    height: 1200px;
  }

  /* Spine */
  .spine {
    position: absolute;
    left: 150px;
    top: 100px;
    width: 124px;
    height: 1000px;
    background: var(--cover-paper);
    border: 14px solid var(--cover-edge);
    border-right-width: 7px;
    border-radius: 6px 0 0 6px;
  }
  .spine-field {
    position: absolute;
    writing-mode: vertical-rl;
    display: flex;
    align-items: center;
    gap: 6px;
    font-size: 11px;
    color: var(--ink);
    white-space: nowrap;
  }
  .spine-field .field-line {
    width: 1px;
    background: var(--rule);
  }
  .spine-customer { left: 14px; top: 40px; height: 360px; }
  .spine-customer .field-line { height: 260px; }
  .spine-contract { left: 34px; top: 560px; height: 300px; }
  .spine-contract .field-line { height: 150px; }
  .spine-title {
    position: absolute;
    left: 48px;
    top: 360px;
    writing-mode: vertical-rl;
    background: var(--accent-blue);
    color: #ffffff;
    font-size: 22px;
    font-weight: 700;
    padding: 6px 2px;
    line-height: 1;
    white-space: nowrap;
  }

  /* Front cover */
  .cover {
    position: absolute;
    left: 274px;
    top: 100px;
    width: 776px;
    height: 1000px;
    background: var(--cover-paper);
    border: 14px solid var(--cover-edge);
    border-left-width: 7px;
    border-radius: 0 6px 6px 0;
  }
  .brand {
    position: absolute;
    left: 100px;
    top: 150px;
    display: flex;
    flex-direction: column;
    align-items: center;
    gap: 14px;
  }
  .brand-art {
    width: 150px;
    height: 90px;
    background: linear-gradient(180deg, var(--art-light) 0%, var(--art-dark) 100%);
  }
  .brand-name {
    font-size: 16px;
    font-weight: 400;
    letter-spacing: 0.5px;
    color: var(--brand-grey);
    text-transform: uppercase;
    white-space: nowrap;
  }
  .chapter-title {
    position: absolute;
    left: 72px;
    top: 400px;
    width: 610px;
    padding: 8px 0 6px;
    background: var(--accent-blue);
    color: #ffffff;
    font-size: 66px;
    font-weight: 700;
    line-height: 1.1;
    text-align: center;
    white-space: nowrap;
  }
  .title-rule {
    position: absolute;
    left: 72px;
    top: 510px;
    width: 610px;
    height: 1px;
    background: var(--rule);
  }
  .field {
    position: absolute;
    left: 72px;
    width: 610px;
    display: flex;
    align-items: flex-end;
    gap: 6px;
    font-size: 14px;
    color: var(--ink);
    white-space: nowrap;
  }
  .field .field-line {
    flex: 1;
    height: 1px;
    background: var(--rule);
    margin-bottom: 3px;
  }
  .field-customer { top: 580px; }
  .field-contract { top: 650px; }
</style>
</head>
<body>
  <main class="canvas">
    <aside class="spine">
      <div class="spine-field spine-customer">
        <span class="field-label">Customer name:</span>
        <span class="field-line"></span>
      </div>
      <div class="spine-title">ADMINISTRATION</div>
      <div class="spine-field spine-contract">
        <span class="field-label">Contract no/Serial no.:</span>
        <span class="field-line"></span>
      </div>
    </aside>
    <section class="cover">
      <div class="brand">
        <div class="brand-art" role="img" aria-label="Brand illustration of business people in front of city buildings"></div>
        <span class="brand-name">Northline Advisory</span>
      </div>
      <h1 class="chapter-title">ADMINISTRATION</h1>
      <div class="title-rule"></div>
      <div class="field field-customer">
        <span class="field-label">Customer name:</span>
        <span class="field-line"></span>
      </div>
      <div class="field field-contract">
        <span class="field-label">Contract no/Serial no.:</span>
        <span class="field-line"></span>
      </div>
    </section>
  </main>
</body>
</html>
```